Social Media Graphics - ALL TEXT RK

We are looking for a series of social media graphics for Instagram (standard size 1:1 (1080x1080px) that are ALL TEXT. We want the following quotes below on each graphic; one quote per graphic. AND, In very small letters at the bottom of each graphic, add @RKMarlowLive

The look and feel of these graphics should be complimentary to the color palette attached below; but keep them simple. But the design is up to you; at the end of this document, I provided various samples of all text graphics that I like as examples.

Target Market(s)

women looking to lose weight

Industry/Entity Type

health and wellness

Colors
E54698
E96AAD
F1A4CE
F9D9EA
FCEFF6

Requirements
Must have
• the quotes in the document
Should not have
• no stock photography

```html
<!DOCTYPE html>
<html lang="en">
<head>
<meta charset="utf-8">
<title>All-Text Social Graphics — RK</title>
<link rel="stylesheet" href="https://fonts.googleapis.com/css2?family=Rubik:wght@500;700;800&display=swap">
<style>
  :root {
    --page-light: #ffffff;
    --page-dark: #bdbdbd;
    --tile-top: #ef79b5;
    --tile-mid: #e54698;
    --tile-bottom: #c00a5c;
    --ink: #ffffff;
    --ink-shadow: rgba(110, 0, 45, 0.55);
    --handle: #fcdcea;
  }
  * { margin: 0; padding: 0; box-sizing: border-box; }
  html, body { width: 1200px; height: 1000px; overflow: hidden; }
  body {
    position: relative;
    background: linear-gradient(110deg, var(--page-light) 0%, #f1f1f1 40%, var(--page-dark) 100%);
    font-family: "Rubik", "Arial Black", sans-serif;
  }
  .post {
    position: absolute;
    width: 258px;
    height: 260px;
    background: linear-gradient(180deg, var(--tile-top) 0%, var(--tile-mid) 45%, var(--tile-bottom) 100%);
    box-shadow: 4px 5px 8px rgba(0, 0, 0, 0.35);
    color: var(--ink);
    display: flex;
    flex-direction: column;
    align-items: center;
  }
  .quote {
    margin-top: 20px;
    height: 200px;
    display: flex;
    flex-direction: column;
    justify-content: center;
    text-align: center;
    font-weight: 800;
    line-height: 1.08;
    text-shadow: 2px 2px 0 var(--ink-shadow);
    white-space: nowrap;
  }
  .quote span { display: block; }
  .quote b { font-weight: 800; }
  .handle {
    position: absolute;
    bottom: 16px;
    font-size: 10px;
    font-weight: 500;
    color: var(--handle);
  }
</style>
</head>
<body>

<div class="post" style="left:46px;top:86px">
  <p class="quote">
    <span style="font-size:21px">Wake up tomorrow</span>
    <span style="font-size:21px">with a flatter belly -</span>
    <span style="font-size:21px">yes, this overnight</span>
    <span style="font-size:21px">remedy works like</span>
    <span style="font-size:54px">magic!</span>
  </p>
  <span class="handle">@RKMarlowLive</span>
</div>

<div class="post" style="left:328px;top:86px">
  <p class="quote">
    <span style="font-size:19px"><b style="font-size:29px">Struggling</b> with</span>
    <span style="font-size:18px">bloating and belly fat?</span>
    <span style="font-size:16px">Try this natural solution</span>
    <span style="font-size:14px">tonight, and wake up feeling</span>
    <span style="font-size:56px">lighter!</span>
  </p>
  <span class="handle">@RKMarlowLive</span>
</div>

<div class="post" style="left:611px;top:86px">
  <p class="quote">
    <span style="font-size:23px">One supplement,</span>
    <span style="font-size:38px">one night;</span>
    <span style="font-size:25px">your belly bloat</span>
    <span style="font-size:23px">could be gone by</span>
    <span style="font-size:40px">morning.</span>
    <span style="font-size:16px">Here's how it works!</span>
  </p>
  <span class="handle">@RKMarlowLive</span>
</div>

<div class="post" style="left:894px;top:86px">
  <p class="quote">
    <span style="font-size:23px">Finally - a natural</span>
    <span style="font-size:31px">solution that</span>
    <span style="font-size:52px">flattens</span>
    <span style="font-size:17px">your belly AND eases</span>
    <span style="font-size:25px">stomach bloat</span>
  </p>
  <span class="handle">@RKMarlowLive</span>
</div>

<div class="post" style="left:46px;top:370px">
  <p class="quote">
    <span style="font-size:20px">Sis, your hormones</span>
    <span style="font-size:20px">are out of whack -</span>
    <span style="font-size:26px">that's why the</span>
    <span style="font-size:54px">weight</span>
    <span style="font-size:26px">won't budge!</span>
  </p>
  <span class="handle">@RKMarlowLive</span>
</div>

<div class="post" style="left:328px;top:370px">
  <p class="quote">
    <span style="font-size:25px">Frustrated with</span>
    <span style="font-size:50px">belly fat</span>
    <span style="font-size:21px">that won't budge?</span>
    <span style="font-size:19px">I've got the solution</span>
    <span style="font-size:15px">that finally worked for me -</span>
    <span style="font-size:15px">no crazy diets required.</span>
  </p>
  <span class="handle">@RKMarlowLive</span>
</div>

<div class="post" style="left:611px;top:370px">
  <p class="quote">
    <span style="font-size:28px">That stubborn</span>
    <span style="font-size:50px">belly fat</span>
    <span style="font-size:25px">isn't your fault -</span>
    <span style="font-size:35px">here's what</span>
    <span style="font-size:27px">no one tells you.</span>
  </p>
  <span class="handle">@RKMarlowLive</span>
</div>

<div class="post" style="left:894px;top:370px">
  <p class="quote">
    <span style="font-size:19px">You've been lied to -</span>
    <span style="font-size:21px">'just <b style="font-size:35px">eat less</b></span>
    <span style="font-size:31px">and exercise</span>
    <span style="font-size:64px">more'</span>
    <span style="font-size:14px">doesn't work in menopause</span>
  </p>
  <span class="handle">@RKMarlowLive</span>
</div>

<div class="post" style="left:329px;top:654px">
  <p class="quote">
    <span style="font-size:23px">A natural way to</span>
    <span style="font-size:33px">boost GLP-1 -</span>
    <span style="font-size:12px">no injections, no side effects, just</span>
    <span style="font-size:33px">real results.</span>
    <span style="font-size:19px">Here's how it works</span>
  </p>
  <span class="handle">@RKMarlowLive</span>
</div>

<div class="post" style="left:612px;top:654px">
  <p class="quote">
    <span style="font-size:21px">GLP-1: the magic</span>
    <span style="font-size:13px">behind the weight loss drugs.</span>
    <span style="font-size:26px">But here's the</span>
    <span style="font-size:54px">secret -</span>
    <span style="font-size:15px">you can boost it naturally</span>
    <span style="font-size:15px">without a prescription!</span>
  </p>
  <span class="handle">@RKMarlowLive</span>
</div>

</body>
</html>
```